Pelkman Agency (http://pa.quorvexstudio.com/)

We are looking for a similar design to what we have, but more professional looking and cleaned up with links and logo that is not so grainy looking. We are an independent insurance agency marketing to personal and commercial clients. We offer all commercial lines markets and all personal lines. We target excavators, landscapers, restaurants, golf courses, contractors. Please look at http://pa.quorvexstudio.com/ which we had designed but do not like it, it will give you an idea of what we are looking for.

Target Market(s)

Commercial and personal insurance. All business products and all personal (homeowners, auto, antique auto, umbrella)

Industry/Entity Type

It Professional

Logo Text

Knowledge Building Your Assurance

Number of Pages Required

5+ page

Colors
000000
848484
0255a3

```html
<!DOCTYPE html>
<html lang="en">
<head>
<meta charset="utf-8">
<title>Pelkman Agency</title>
<link href="https://fonts.googleapis.com/css2?family=Exo+2:wght@300;400;500;600&family=Roboto:wght@400;700&display=swap" rel="stylesheet">
<style>
:root{
  --blue:#0c75cc;
  --navy:#0f2338;
  --sky:#3aa9dc;
  --orange:#f0632a;
  --magenta:#d6175f;
  --teal:#2f9fc4;
  --ink:#1c2a3a;
  --grey:#8a8a8a;
  --body-blue:#5a8fc2;
  --rule:#e3e3e3;
  --panel:#dfe6ec;
}
*{box-sizing:border-box;margin:0;padding:0}
html,body{width:1200px;height:1000px;overflow:hidden;background:#fff;font-family:"Exo 2",sans-serif}
.page{position:relative;width:1200px;height:1000px;overflow:hidden}
.topbar{position:absolute;left:0;top:0;width:1200px;height:30px;background:var(--blue)}
.topbar .phone-cell{position:absolute;left:232px;top:0;width:28px;height:30px;border-left:1px solid rgba(255,255,255,.25);border-right:1px solid rgba(255,255,255,.25)}
.topbar .callline{position:absolute;left:271px;top:9px;font:400 9.5px Roboto,sans-serif;color:#fff}
.topbar .callline b{font-weight:700}
.social{position:absolute;left:880px;top:0;display:flex}
.social span{width:24px;height:30px;border-left:1px solid rgba(255,255,255,.3);display:flex;align-items:center;justify-content:center}
.social span:last-child{border-right:1px solid rgba(255,255,255,.3);width:30px}
.social i{width:9px;height:9px;background:#fff;border-radius:50%}
.darkband{position:absolute;left:0;top:30px;width:1200px;height:293px;background:var(--navy);border-bottom:3px solid var(--blue)}
.brand{position:absolute;left:240px;top:38px;font:600 19px "Exo 2",sans-serif;color:var(--sky)}
.nav{position:absolute;top:43px;left:632px;display:flex;gap:18px;align-items:center;font:400 11px Roboto,sans-serif;color:#fff}
.hero{position:absolute;left:232px;top:68px;width:737px;height:315px;border:2px solid var(--blue);border-top:0;overflow:hidden;background:var(--panel)}
.hero .photo{position:absolute;left:230px;top:0;width:507px;height:315px;background:linear-gradient(135deg,#b9bfc4 0%,#a6a596 55%,#8d937f 100%)}
.hero .kicker{position:absolute;left:44px;top:34px;font:300 20px "Exo 2",sans-serif;color:var(--orange)}
.hero h1{position:absolute;left:44px;top:55px;font:600 22px "Exo 2",sans-serif;color:var(--ink)}
.hero .intro{position:absolute;left:44px;top:89px;width:225px;font:300 8.5px/13px "Exo 2",sans-serif;color:#555}
.icons{position:absolute;left:46px;top:155px;display:flex;gap:8px}
.icons span{width:30px;height:30px;border-radius:4px;display:flex;align-items:center;justify-content:center}
.hero .callfree{position:absolute;left:44px;top:209px;font:300 19px "Exo 2",sans-serif;color:#fff}
.hero .number{position:absolute;left:44px;top:231px;font:600 21px "Exo 2",sans-serif;color:var(--orange)}
.quote{position:absolute;left:464px;top:56px;width:238px;height:190px;background:rgba(40,55,80,.55);border-radius:2px}
.quote .field{position:absolute;left:13px;width:212px;height:32px;background:#fff;border-bottom:1px solid #ddd;font:italic 300 8px "Exo 2",sans-serif;color:#999;padding:11px 6px}
.quote .btn{position:absolute;left:13px;top:128px;width:212px;height:36px;background:var(--magenta);border-radius:3px;color:#fff;font:400 9.5px "Exo 2",sans-serif;text-align:center;line-height:36px}
.dots{position:absolute;left:0;top:286px;width:66px;height:20px;background:#3b4450;display:flex;gap:3px;align-items:center;padding-left:16px}
.dots i{width:5px;height:5px;background:#fff}
.dots i:first-child{background:var(--sky)}
.arrows{position:absolute;top:284px;left:689px;display:flex;gap:6px}
.arrows span{width:17px;height:22px;background:var(--teal);color:#fff;font:400 12px Roboto,sans-serif;text-align:center;line-height:21px}
.about{position:absolute;left:232px;top:417px;width:736px;text-align:center}
.about h2{font:600 20px "Exo 2",sans-serif;color:var(--ink)}
.about .tag{margin-top:9px;font:300 20.5px "Exo 2",sans-serif;color:#555}
.about .tag b{font-weight:600;color:var(--sky)}
.about p{font:300 11px/14px "Exo 2",sans-serif;color:var(--grey);margin-top:14px}
.about p.lead{margin-top:6px}
.rule{position:absolute;left:0;width:1200px;height:1px;background:var(--rule)}
.section-title{position:absolute;left:231px;font:600 19.5px "Exo 2",sans-serif;color:var(--ink)}
.sidemenu{position:absolute;left:243px;border-left:2px solid var(--blue);padding-left:10px;list-style:none;font:700 9px/26px Roboto,sans-serif;color:#2a7ab8}
.sidemenu .active{color:#333}
.content{position:absolute;left:339px;width:620px}
.content h3{font:300 21px "Exo 2",sans-serif;color:#444}
.content p{font:300 11.3px/13.9px "Exo 2",sans-serif;color:var(--body-blue);margin-top:5px}
.content p+p{margin-top:14px}
.more{position:absolute;right:232px;top:908px;font:300 11.5px "Exo 2",sans-serif;color:var(--body-blue)}
</style>
</head>
<body>
<div class="page">
<header class="topbar">
  <div class="phone-cell"><svg width="28" height="30" viewBox="0 0 28 30"><path d="M9 9c1-1 2-1 3 0l1.5 2.5c.4.7 0 1.3-.6 1.8l-.8.6c.8 1.7 2 2.9 3.7 3.7l.6-.8c.5-.6 1.1-1 1.8-.6L20.5 18c1 1 1 2 0 3l-1 1c-5 0-11-6-11-11z" fill="#fff"/></svg></div>
  <div class="callline">CALL-US-FREE: <b>1-888-4 PELKMN</b></div>
  <div class="social"><span><i></i></span><span><i></i></span><span><i></i></span></div>
</header>
<div class="darkband"></div>
<div class="brand">Pelkman Agency</div>
<nav class="nav"><span>About</span><span>Personal</span><span>Business</span><span>Service Center</span><span>Contact</span>
  <svg width="11" height="11" viewBox="0 0 11 11"><path d="M5.5 1 0 5.5h1.5V10h3V7h2v3h3V5.5H11z" fill="#fff"/></svg></nav>

<section class="hero">
  <div class="photo" role="img" aria-label="Photo of a two-storey family house with siding, lawn and shrubs, overlaid with a blue angled graphic"></div>
  <div class="kicker">Home</div>
  <h1>INSURANCE</h1>
  <p class="intro">Lorem ipsum dolor sit amet, consetetur sadipscing elitr, sed diam nonumy eirmod tempor invidunt ut labore et dolore magna aliquyam erat, sed diam voluptua.</p>
  <div class="icons">
    <span style="background:var(--orange)"><svg width="16" height="14" viewBox="0 0 16 14"><path d="M8 1 1 7h2v6h4V9h2v4h4V7h2z" fill="#fff"/></svg></span>
    <span style="background:var(--magenta)"><svg width="14" height="14" viewBox="0 0 14 14"><path d="M5 0h4v5h5v4H9v5H5V9H0V5h5z" fill="#fff"/></svg></span>
    <span style="background:var(--blue)"><svg width="18" height="14" viewBox="0 0 18 14"><path d="M3 6l2-4h8l2 4h2v5h-2v2h-3v-2H6v2H3v-2H1V6z" fill="#fff"/><circle cx="5" cy="8.5" r="1.2" fill="#0c75cc"/><circle cx="13" cy="8.5" r="1.2" fill="#0c75cc"/></svg></span>
    <span style="background:var(--navy)"><svg width="16" height="14" viewBox="0 0 16 14"><path d="M5 2V1h6v1h4v11H1V2zm1 0h4V1.8H6z" fill="#fff"/><rect x="1" y="6" width="14" height="1" fill="#0f2338"/></svg></span>
  </div>
  <div class="callfree">CALL-US-FREE</div>
  <div class="number">1-888-4 PELKMN</div>
  <form class="quote">
    <div class="field" style="top:26px">Name</div>
    <div class="field" style="top:58px">Email</div>
    <div class="field" style="top:90px">Phone</div>
    <div class="btn">GET A FREE QUOTE</div>
  </form>
  <div class="dots"><i></i><i></i><i></i><i></i></div>
  <div class="arrows"><span>«</span><span>»</span></div>
</section>

<section class="about">
  <h2>About Pelkman Agency</h2>
  <div class="tag"><b>SMALL</b> ENOUGH TO CARE, <b>BIG</b> ENOUGH TO MAKE A DIFFERENCE</div>
  <p class="lead">Established in 1950 by the Hale family, the Pelkman Agency was founded on the philosophy of offering personal, professional service. Since then we have grown into a full service agency with a staff of 10 insurance specialist serving over 2,000 individuals and 800 businesses.</p>
  <p>We are an Independent Agency , which allows us to keep your needs in mind.</p>
  <p>We do not work for an insurance company we work for you. we work on your side when you have a loss and follow through to see that you get affair, prompt, payment. We represent a carefully selected group of reputable insurance companies, and we place your policy with the company offering the best coverage at the best possible price.</p>
  <p>Please explore our website and let us know how we can help serve your insurance needs.</p>
</section>

<div class="rule" style="top:662px"></div>
<h2 class="section-title" style="top:675px">Personal Insurance</h2>
<ul class="sidemenu" style="top:712px">
  <li class="active">Annuity</li><li>Auto</li><li>Home</li><li>Life</li><li>Long Term Care</li>
</ul>
<article class="content" style="top:710px">
  <h3>Annuities May Be a Smart Fit for Your Investment Plan</h3>
  <p>Lorem ipsum dolor sit amet, charetra varius quam sit amet vulputate. Quisque mauris augue, molestie tincidunt condimentum vitae, gravida a libero.Lorem ipsum dolor sit amet, charetra varius quam sit amet vulputate. Quisque mauris augue, molestie tincidunt condimentum vitae, gravida a libero.Lorem ipsum dolor sit amet, charetra varius quam sit amet vulputate. Quisque mauris augue, molestie tincidunt condimentum vitae, gravida a libero.Lorem ipsum dolor sit amet, charetra varius quam sit amet vulputate. Quisque mauris augue, molestie tincidunt condimentum vitae, gravida a libero.</p>
  <p>Lorem ipsum dolor sit amet, charetra varius quam sit amet vulputate. Quisque mauris augue, molestie tincidunt condimentum vitae, gravida a libero.Lorem ipsum dolor sit amet, charetra varius quam sit amet vulputate. Quisque mauris augue, molestie tincidunt condimentum vitae, gravida a libero.Lorem ipsum dolor sit amet, charetra varius quam sit amet vulputate. Quisque mauris augue, molestie tincidunt condimentum vitae, gravida a libero.Lorem ipsum dolor sit amet, charetra varius quam sit amet vulputate. Quisque mauris augue, molestie tincidunt condimentum vitae, gravida a libero.</p>
</article>
<a class="more">Start a annuity claim ▸</a>

<div class="rule" style="top:936px"></div>
<h2 class="section-title" style="top:948px">Business Insurance</h2>
<ul class="sidemenu" style="top:985px">
  <li class="active">Carpenters</li>
</ul>
<article class="content" style="top:984px">
  <h3>Get An Online Carpenters Insurance Quote</h3>
</article>
</div>
</body>
</html>
```